Restorative Fitness & Nutrition eBook

This is a simple nutrition ebook called Kindlewave. Designed to be download by athletes and fitness enthusiasts who want to improve their athletic performance and recovery after workouts.

This is one of 7 x e-book drafts ready to be designed up.

3 of them (including Kindlewave) are only 3-4 pages long, the other 4 ebooks are much longer and more comprehensive (15-40pages).

I am a restorative health and fitness coach based in Sydney. I work closely with athletes (runners and triathletes) to improve flexibility, core strength, breathing and mindset. I incorporate practices such as yoga, pilates, self-myofascial release, nutrition and meditation.

The ebooks will be available for purchase online and used for home study or training by my clients. They will have instructional photos and copy.

Target Market(s)

Everyday athletes. Runners. Triathletes. Swimmers. Fitness enthusiasts. Health conscious individuals. Aged between 30-50. A mix of male and female, but mostly women.

Industry/Entity Type

Fitness

Font styles to use
Sans Serif
Other font styles liked:
• Freeland Font

Requirements
Must have
• - Be visually beautiful using imagery supplied. I have more if needed.
• - The copy included
• - My logo
• - Short and sweet style. No more than 5 pages. Ideally 3-4
• - Light, white and fresh look
• - Clear and easy to read
Should not have
• Dark black themes
• Squishy text and no white space.

```html
<!DOCTYPE html>
<html lang="en">
<head>
<meta charset="utf-8">
<title>Kindlewave – 7 Days on My Plate</title>
<link href="https://fonts.googleapis.com/css2?family=Montserrat:ital,wght@0,400;0,700;0,800;0,900;1,700&family=Raleway:wght@300;400&family=Josefin+Sans:wght@400;600&family=Allura&display=swap" rel="stylesheet">
<style>
  :root{
    --paper:#ffffff;
    --ink:#2b2b2b;
    --muted:#8a8a8a;
    --quote-blue:#1f6fc4;
    --band-grey:#a6aab6;
    --mon:#e6c11b;
    --tue:#e2474f;
    --wed:#6ab443;
    --thu:#f0781d;
    --fri:#2c6db4;
    --sat:#6b3f9c;
    --sun:#e1303a;
    --snack:#f39d1c;
    --drink:#58ae48;
    --gap:#f4f4f4;
  }
  *{box-sizing:border-box;margin:0;padding:0}
  html,body{width:1200px;height:2661px;overflow:hidden;background:var(--paper)}
  body{position:relative;font-family:"Josefin Sans",sans-serif;color:var(--ink)}
  .abs{position:absolute}

  /* Cover page */
  .cover-photo{left:0;top:0;width:536px;height:455px;background:linear-gradient(160deg,#dfe8ef 0%,#c9d3da 40%,#b9875a 75%,#8e6a4b 100%)}
  .cover-info{left:560px;top:26px;width:640px;text-align:center}
  .quote{font-family:"Montserrat",sans-serif;font-weight:700;font-style:italic;color:var(--quote-blue);font-size:27px;line-height:1.2;text-transform:uppercase}
  .quote-by{font-size:20px;margin-top:6px}
  .info-head{font-family:"Montserrat",sans-serif;font-weight:800;font-size:16px;text-transform:uppercase;margin-top:26px}
  .info-line{font-size:15px;line-height:1.45}

  .title{left:160px;top:488px;z-index:2;font-family:"Montserrat",sans-serif;font-weight:900;font-size:56px;letter-spacing:0;line-height:1;white-space:nowrap}
  .subtitle{left:164px;top:568px;z-index:2;font-family:"Raleway",sans-serif;font-weight:300;font-size:27px;line-height:1.25;text-transform:uppercase;color:#4a4a4a}
  .name-band{left:0;top:745px;width:598px;height:77px;background:var(--band-grey)}
  .name-band span{position:absolute;left:162px;top:6px;font-family:"Allura",cursive;font-size:54px;color:#fff}
  .hands-photo{left:604px;top:505px;width:596px;height:343px;z-index:1;background:radial-gradient(circle at 22% 45%,#5c4a3c 0 13%,transparent 14%),radial-gradient(circle at 62% 70%,#b69c7c 0 17%,transparent 18%),linear-gradient(120deg,#f6f3f0,#e9ddd2)}

  .page-gap{left:0;height:6px;width:1200px;background:var(--gap)}

  /* Meal plan pages */
  .col{text-align:center;font-size:12.4px;line-height:1.38;z-index:2}
  .day{font-family:"Montserrat",sans-serif;font-weight:800;font-size:23px;text-transform:uppercase;line-height:1.1;margin-top:14px}
  .day:first-child{margin-top:0}
  .meal{font-family:"Montserrat",sans-serif;font-weight:700;font-style:italic;font-size:11.5px;color:var(--muted);text-transform:uppercase;letter-spacing:1px;margin-top:10px}
  .day + .meal{margin-top:0}
  .dish{text-decoration:underline;font-size:13px}
  .col p{margin:0}
  .mon{color:var(--mon)} .tue{color:var(--tue)} .wed{color:var(--wed)} .thu{color:var(--thu)}
  .fri{color:var(--fri)} .sat{color:var(--sat)} .sun{color:var(--sun)}
  .snack{color:var(--snack)} .drink{color:var(--drink)}
  .snack-note{font-family:"Montserrat",sans-serif;font-weight:700;font-style:italic;font-size:12px;color:var(--snack);text-transform:uppercase}

  .beans-photo{left:440px;top:1150px;width:330px;height:330px;border-radius:50%;z-index:1;background:radial-gradient(circle,#eef3e6 0%,#d9e4c8 55%,#c8ccc6 100%);opacity:.55}
  .plums-top{left:746px;top:1723px;width:320px;height:170px;border-radius:0 0 160px 160px;background:radial-gradient(circle at 50% 10%,#5a4a8a,#3b2f66 60%,#5e4c55 100%)}
  .plums-bottom{left:232px;top:2572px;width:304px;height:89px;border-radius:152px 152px 0 0;background:radial-gradient(circle at 50% 90%,#5a4a8a,#3b2f66 60%,#5e4c55 100%)}
</style>
</head>
<body>

<!-- Cover page -->
<div class="abs cover-photo" role="img" aria-label="Photo of a smiling woman holding a bowl, leaning on a seaside boardwalk house"></div>
<div class="abs cover-info">
  <p class="quote">‘Eat food, not too much and<br>mostly plants’</p>
  <p class="quote-by">Arthur Vance</p>
  <p class="info-head" style="margin-top:72px">Learn more</p>
  <p class="info-line">tessamarlow.com</p>
  <p class="info-head">Let’s connect</p>
  <p class="info-line">tessa@tessamarlow.com<br>Facepage @TessaMarlow<br>Snapgram @tessamarlowfit</p>
  <p class="info-head">Let’s work together</p>
  <p class="info-line">1:1 Coaching | Online Coaching | Workshops | E-Resources</p>
</div>

<h1 class="abs title">KINDLEWAVE</h1>
<p class="abs subtitle">7-days on my plate<br>nourishing recipes to feed<br>your tired and hungry<br>muscles.</p>
<div class="abs name-band"><span>Tessa Marlow</span></div>
<div class="abs hands-photo" role="img" aria-label="Overhead photo of hands holding a cup of coffee and a bowl of granola"></div>

<div class="abs page-gap" style="top:848px"></div>

<!-- Page 2 -->
<div class="abs beans-photo" role="img" aria-label="Colander of fresh green beans"></div>

<div class="abs col" style="left:120px;top:930px;width:500px">
  <h2 class="day mon">Monday</h2>
  <p class="meal">Breakfast</p>
  <p class="dish">Power Protein Smoothie</p>
  <p>I blend up 1 serving of protein powder, ½ tsp. of ground cinnamon, 1 tbsp. of chia seeds, ½ cup frozen berries, ½ frozen banana, ½ cup spinach leaves and 1 cup of nut or coconut milk.</p>
  <p class="meal">Lunch</p>
  <p class="dish">Superfood Bowl</p>
  <p>I chop and roast sweet potato and eggplant; steam shredded kale and chopped broccoli; and mix chopped coriander and mint through cooked quinoa. Add all cooked ingredients to a bowl, drizzle with tahini, top with chopped almonds and a tbsp. of sauerkraut. It’s a big dose of vitamins, protein and gut lovin goodness.</p>
  <p class="meal">Dinner</p>
  <p class="dish">Soba Noodle Special</p>
  <p>I steam snow peas and frozen green edamame, spiralise a fresh carrot, and mix it all through cooked buckwheat soba noodles. I make a yummy Asian dressing by mixing ¼ cup tamari, 1 tbsp peanut butter, 1 tsp ginger, 1 tsp sesame oil, and the juice of a lime, and then I stir it through the noodles and veg and season with chopped coriander and toasted sesame seeds. Add some cooked tempeh or wild caught grilled salmon for extra protein.</p>
  <h2 class="day tue">Tuesday</h2>
  <p class="meal">Breakfast</p>
  <p class="dish">Overnight Oats</p>
  <p>The night before I blend 1 banana with 1 tbsp. chia seeds, 1tsp. cinnamon, 1 serving of protein powder, ½ tbsp. of cacao powder and 1 cup of nut milk or water. Then I pour it in a jar and stir through ⅓ cup of oats. After letting it soak overnight, I enjoy it after my morning run.</p>
  <p class="meal">Lunch</p>
  <p class="dish">Falafel Wrap</p>
  <p>I spread beetroot and hummus dip on a Lebanese bread wrap, and then I fill it with lots of salad goodness (spinach, tomato, cucumber, sauerkraut, pickles, grated carrot) and 2-3 warm falafel balls. Wrap, eat and enjoy!</p>
  <p class="meal">Dinner</p>
  <p class="dish">Mexican Bowl</p>
  <p>I cook brown rice and my red kidney bean chili (1-can red kidney beans, ½ diced brown onion, 1 tsp. garlic, 1 grated zucchini, 1 grated carrot, 1 can of diced tomatoes, ½ tsp. chili powder). I fill a bowl with a serving of cooked brown rice, kidney bean chili, a handful of spinach leaves, chopped coriander and a huge dollop of my famous guacamole!</p>
</div>

<div class="abs col" style="left:650px;top:930px;width:500px">
  <h2 class="day wed">Wednesday</h2>
  <p class="meal">Breakfast</p>
  <p class="dish">Toast and Banana</p>
  <p>I toast some soughdough bread and top it with with peanut or almond butter and sliced banana. Easy peasy!</p>
  <p class="meal">Lunch</p>
  <p class="dish">Salad and Mixed Bean Wrap</p>
  <p>I spread beetroot and hummus dip on a Lebanese bread wrap, and then I fill it with lots of salad goodness (spinach, tomato, cucumber, sauerkraut, pickles, grated carrot) and any leftover beans I may have (the four-bean mix is great!).</p>
  <p class="meal">Dinner</p>
  <p class="dish">Roast Veggie Red Curry with Quinoa</p>
  <p>I chop and roast sweet potato and sliced red capsicum, then I steam green peas and broccoli florets. I gently fry 2 tbsp. of red curry paste with 1 can of coconut milk then I add all the cooked veggies and let it simmer for 10-mins. Spoon it over cooked quinoa and garnish with chopped coriander.</p>
  <h2 class="day thu">Thursday</h2>
  <p class="meal">Breakfast</p>
  <p class="dish">Power Protein Smoothie</p>
  <p>I blend up 1 serving of protein powder, ½ tsp. of ground cinnamon, 1 tbsp. of chia seeds, ½ cup frozen berries, ½ frozen banana, ½ cup spinach leaves and 1 cup of nut or coconut milk.</p>
  <p class="meal">Lunch</p>
  <p class="dish">Stuffed Sweet Potato</p>
  <p>I wash a small sweet potato (keep the skin on). With a fork, poke holes all over potato and wrap in a paper towel. I microwave the sweet potato on high for about 8 minutes, or until tender all the way to the center. Cut the potato in half and top it with a handful of rocket and canned lentils. Microwave uncovered for 30 seconds to wilt rocket and warm lentils. Top with cinnamon, dried thyme, dried cranberries, pumpkin seeds and a drizzle of olive oil.</p>
  <p class="meal">Dinner</p>
  <p class="dish">Spaghetti with Green Pesto and Roast Cherry Tomatoes</p>
  <p>I cook a serving of whole-wheat spaghetti and roast a handful of cherry tomatoes in the oven. In a bowl I add the cooked pasta, the roast cherry tomatoes and stir through 2-heaped tbsp. of my homemade pesto. Add a squeeze of lemon and salt and pepper to finish.</p>
</div>

<div class="abs page-gap" style="top:1723px"></div>

<!-- Page 3 -->
<div class="abs plums-top" role="img" aria-label="Bowl of fresh purple plums"></div>
<div class="abs plums-bottom" role="img" aria-label="Bowl of fresh purple plums"></div>

<div class="abs col" style="left:120px;top:1845px;width:530px">
  <h2 class="day fri">Friday</h2>
  <p class="meal">Breakfast</p>
  <p class="dish">Gluten Free Granola</p>
  <p>I start the day with ½ cup of my homemade gluten free granola, topped with fresh berries, seeds, coconut yoghurt and almond milk.</p>
  <p class="meal">Lunch</p>
  <p class="dish">Spinach, Roast Pumpkin and Chickpea Salad</p>
  <p>I roast chopped pumpkin that has been seasoned with salt, pepper and cumin. Then I mix baby spinach, canned chickpeas, finely sliced red onion, chopped figs and the roast pumpkin in a bowl. After mixing all together, I season with chopped coriander, olive oil and salt and pepper.</p>
  <p class="meal">Dinner</p>
  <p class="dish">Veggie Pad Thai</p>
  <p>Stir-fry matchstick cut carrot sticks, red capsicum sticks and broccoli florets in coconut oil. Cook rice noodles as per directions and mix ingredients together with my favourite Asian dressing, ¼ cup tamari, 1 tbsp. peanut butter, 1 tsp. ginger, 1 tsp. sesame oil, and the juice of a lime. Then I season with chopped coriander and chopped spring onions. Add some cooked tempeh or lean grilled chicken for extra protein.</p>
  <h2 class="day sat">Saturday</h2>
  <p class="meal">Breakfast</p>
  <p class="dish">Green Machine</p>
  <p>I scramble 2 free range eggs with 1-heaped tbsp. of my homemade pesto. Serve with soughdough toast and avocado, et voila!</p>
  <p class="meal">Lunch</p>
  <p class="dish">Sushi</p>
  <p>Lunch is on the go today and I choose take-away brown rice and vegetable sushi.</p>
  <p class="meal">Dinner</p>
  <p class="dish">Homemade Burger and Chips</p>
  <p>I make sweet potato and lentil patties and build a burger on a wholegrain roll with salad greens, sliced tomato, beetroot, pickles and cucumber. You can also roast some homemade potato fries on the side if you’re starving. Every now and then I’ll use lean beef mince instead of the beans if I need more iron.</p>
</div>

<div class="abs col" style="left:660px;top:1920px;width:530px">
  <h2 class="day sun">Sunday</h2>
  <p class="meal">Breakfast</p>
  <p class="dish">Buckwheat Banana Pancakes</p>
  <p>Blend well all ingredients: 1 cup nut or coconut milk, 1 ripe banana, 1/2 tsp. vanilla, 1 tbsp. coconut oil, 1 cup buckwheat flour, 1 tsp. baking powder and a pinch of sea salt, pinch of sea salt. Cook both sides using some baking paper on skillet or pan then top it with maple syrup, coconut yoghurt, seeds and sprinkle with cinnamon.</p>
  <p class="meal">Lunch</p>
  <p class="dish">Left Overs</p>
  <p>I eat the left over burger patties from last night with a green salad on the side.</p>
  <p class="meal">Dinner</p>
  <p class="dish">Roast Veggie Lasagna</p>
  <p>This is one for the family. I roast a stack of vegetables (sweet potato, pumpkin, zucchini, capsicum, eggplant). Then I layer a baking dish with the roast veggies, tomato passata sauce, spinach leaves and whole-wheat lasagna sheets. To finish I top with a ricotta and Parmesan cheese.</p>
  <h2 class="day snack">Snacks</h2>
  <p class="snack-note">If I’m on the run or feeling extra hungry I reach for:</p>
  <p>Fresh carrot sticks with hummus<br>Brown rice crackers with either almond/peanut butter, avocado or hummus spread on top<br>A piece of whole fruit...whatever is in season<br>A handful of mixed nuts and seeds<br>2 x fresh dates. I like to take the pit out and stuff a macadamia in the middle<br>A few tablespoons of coconut yoghurt with fresh berries and a sprinkle of cinnamon</p>
  <h2 class="day drink">Drinks</h2>
  <p>I drink water, and lots of it.<br>Earl grey tea in the morning and decaf green tea in the afternoon.<br>On the weekends I usually have a green juice with lots of fruit and veggies for a potent vitamin hit<br>I love a glass of wine with dinner on the weekends</p>
</div>

</body>
</html>
```